Brazilian publishing house needs a JAZZY poster

We're launching an international guerrilla marketing campaign for a biography about the greatest saxophonist ever, Walter Dunmore (also known as "Comet"), so we need a poster that will be printed and pasted on walls and posts, on a regular sheet, size A4.

It must say "Comet vive!" (which means "Comet lives!" in Portuguese) and have the website, www.zuvalink.net/cometvive. All the rest is free. Jazzy, MINIMALIST, cool images with birds and saxophones (or birds becoming saxophones) are welcome. Also, please insert our logo (attached) somewhere, even if not big.

I like this campaign very much and you like something like that: https://quillotavespers.blogfolio.net/

Hope to hear from you!

Marketing

• Easy to see and understand, like most guerrilla actions, without many colors

```html
<!DOCTYPE html>
<html lang="pt">
<head>
<meta charset="utf-8">
<title>Comet vive!</title>
<link rel="stylesheet" href="https://fonts.googleapis.com/css2?family=Rubik+Dirt&family=Open+Sans:wght@400&display=swap">
<style>
  :root {
    --magenta-deep: #6e0a38;
    --magenta: #c0135f;
    --magenta-bright: #e0267a;
    --pink-glow: #f9d3e4;
    --pink-soft: #f2a0c4;
    --white: #ffffff;
    --crowd-dark: #3e0820;
    --crowd-mid: #a81c58;
    --suit-light: rgba(178, 182, 160, 0.9);
    --suit-dark: rgba(92, 90, 70, 0.9);
  }
  html, body {
    margin: 0;
    padding: 0;
    width: 800px;
    height: 1200px;
    overflow: hidden;
    background: var(--magenta-deep);
  }
  .poster {
    position: relative;
    width: 800px;
    height: 1200px;
    overflow: hidden;
    background:
      radial-gradient(ellipse 480px 380px at 430px 500px, var(--pink-glow) 0%, var(--pink-soft) 35%, var(--magenta-bright) 72%, transparent 100%),
      linear-gradient(180deg, var(--magenta) 0%, var(--magenta-bright) 45%, var(--magenta) 75%, var(--magenta-deep) 100%);
  }
  .crowd-scene {
    position: absolute;
    left: 0;
    top: 600px;
    width: 800px;
    height: 600px;
    background:
      radial-gradient(ellipse 260px 200px at 80px 420px, rgba(62, 8, 32, 0.7) 0%, transparent 100%),
      radial-gradient(ellipse 260px 220px at 740px 480px, rgba(62, 8, 32, 0.7) 0%, transparent 100%),
      linear-gradient(180deg, rgba(168, 28, 88, 0) 0%, var(--crowd-mid) 35%, var(--crowd-dark) 100%);
  }
  .performer {
    position: absolute;
    left: 200px;
    top: 545px;
    width: 440px;
    height: 680px;
    border-radius: 150px 190px 0 0;
    background: linear-gradient(160deg, var(--suit-light) 0%, var(--suit-dark) 100%);
  }
  .headline {
    position: absolute;
    left: 0;
    width: 800px;
    margin: 0;
    text-align: center;
    font-family: "Rubik Dirt", "Impact", sans-serif;
    font-weight: 400;
    line-height: 1;
    text-transform: uppercase;
    transform-origin: 50% 0;
  }
  .headline-name {
    top: 20px;
    font-size: 172px;
    letter-spacing: 0;
    color: var(--white);
    transform: scaleY(1.5);
  }
  .headline-verb {
    top: 258px;
    font-size: 236px;
    letter-spacing: 2px;
    color: var(--magenta);
    transform: scaleY(1.35);
  }
  .footer-url {
    position: absolute;
    left: 30px;
    bottom: 22px;
    margin: 0;
    font-family: "Open Sans", Arial, sans-serif;
    font-size: 26px;
    color: var(--white);
  }
  .publisher-name {
    position: absolute;
    right: 24px;
    bottom: 20px;
    margin: 0;
    font-family: "Open Sans", Arial, sans-serif;
    font-weight: 400;
    font-size: 30px;
    letter-spacing: 3px;
    color: var(--white);
  }
</style>
</head>
<body>
  <main class="poster">
    <div class="crowd-scene" role="img" aria-label="Concert crowd with raised hands under magenta stage light"></div>
    <div class="performer" role="img" aria-label="Saxophonist in a grey suit playing an alto saxophone, flames rising from the bell"></div>
    <h1 class="headline headline-name">Comet</h1>
    <p class="headline headline-verb">Vive!</p>
    <p class="footer-url">www.zuvalink.net/cometvive</p>
    <p class="publisher-name">VALDEMAR</p>
  </main>
</body>
</html>
```